Shop Image re-design

Hi,

We are a company who operate several convenience stores around Northern Ireland, and are currently trading under a generic name of 'lorn'. We have made a decision to re-brand the stores under the name of "The Quiet Fox", and will start the process by intially trialling the new look by converting our flag ship, and busiest shop to evaluate the results. The stops main focus is on fresh convenience foods - Coffee,sandwichs,fruit,fresh pastries,chilled drinks & juices etc but we also sell the usual items you would expect such as newspapers, magazines, greeting cards, snacks, confectionery etc

This store is situated in a busy hospital and we serve upward of 25,000 customers a week - doctors, nurses, support staff,patients and visitors all of whom come from a wide cross section of society so the design and style of the new rebranding will have to be SPECTACULARY good to win!

The Design we are looking for must be very Professional, stylish, modern, eye catching and yet still display a fun,welcoming and friendly image to our customers.

I have Included some image files of the current look and feel of the branding in the store, these include the outside signage, internal graphics and point of sale material. Its a good image and brand we have at the moment but I want something EXCEPTIONAL that will make us stand out from other retailers, and be memorable to the customers!

Some things to consider...

The main design should be for the outside signage (see image attached for shape, position and general size). The design should not be to cluttered, and the name as mentioned before will be "the quiet fox" but additionally for this store the term "hospital shop" should also be added underneath the main title,but in a much smaller size to the overall name.In other shops we will propably change the term "hospital shop" to "newsagents" where this is more appropriate, but we will redesign this when we come to convert these stores in due course.

I think we should still display some general 'product' images on the outside signage as is currently the case, and if any are included the images should be of a very high resolution and quality, and make you want to eat it!
Although Im suggesting we should keep some sort of images please donot stop your creative processes, if you think something looks good without them...please submit!

The overall 'feel' and style of the outside sign should flow through into the shop with the internal '3d' signage being of a simalar style as well as the point of sale graphics. In submitting for the internal signage please just do so in a 2d format. (see attached images)

The point of sale materal (shelf 'barkers' and a4 posters), that we use around the shop are of a pre-printed coloured card nature that the managers can run through a laser printer to produce store-specific special offers etc. (see attached images)

We are very excited about this re-branding, as we have used artmarketo before to help us design our company stationery etc., with great results! We therefore hope all you talented designers out there can help us make it a reality... so let your creative juices flow we want something very original!

Thanks,

Rupert.

Target Market(s)

As described in the above brief...
It is worth noting that our stores do not operate in 'value focused' enviroment, we are more more concerned with quality of product and speed and quality of service.

Requirements
Must have
• See detailed design brief above.
Nice to have
• It would be good to have a theme that we can transfer across the store onto uniforms, carrier bags, coffee cups and still fits into the overall 'brand' image
Should not have
• Cartoons or childish style designs or graphics!

```html
<!DOCTYPE html>
<html lang="en">
<head>
<meta charset="utf-8">
<title>The Quiet Fox – Hospital Shop Signage</title>
<link rel="stylesheet" href="https://fonts.googleapis.com/css2?family=Open+Sans:wght@300;700;800&display=swap">
<style>
  :root {
    --ink: #000000;
    --paper: #ffffff;
    --honey: #f0cd00;
    --mist: #eceeed;
    --cream: #fbf5d8;
    --rule: #1a1a1a;
  }
  * { box-sizing: border-box; margin: 0; padding: 0; }
  html, body {
    width: 1200px; height: 901px; overflow: hidden;
    background: var(--paper);
    font-family: "Open Sans", Arial, sans-serif;
  }
  .canvas { position: relative; width: 1200px; height: 901px; }

  /* Shared pieces */
  .brand-mark {
    display: flex; align-items: center; gap: 8px;
    color: var(--ink); font-weight: 800; white-space: nowrap;
  }
  .brand-mark .dot { border-radius: 50%; background: var(--ink); flex: none; }
  .watermark {
    position: absolute; color: var(--mist); font-weight: 800;
    white-space: nowrap; line-height: 1;
  }
  .watermark-disc { position: absolute; border-radius: 50%; background: var(--mist); }
  .accent { color: var(--honey); }

  /* Exterior sign */
  .exterior-sign {
    position: absolute; left: 34px; top: 37px; width: 384px; height: 837px;
    border: 3px solid var(--ink); overflow: hidden; background: var(--paper);
  }
  .exterior-sign .site-band {
    height: 64px; background: var(--ink); color: var(--paper);
    font-weight: 800; font-size: 42px; letter-spacing: -2.5px;
    display: flex; align-items: center; justify-content: center;
  }
  .exterior-sign .watermark-disc { left: 10px; top: 360px; width: 330px; height: 330px; }
  .exterior-sign .watermark-soft { left: 150px; top: 520px; width: 260px; height: 260px; background: var(--cream); }
  .exterior-sign .brand-mark {
    position: absolute; left: 52px; top: 180px; font-size: 22px; flex-direction: column; gap: 10px;
  }
  .exterior-sign .brand-mark .dot { width: 70px; height: 70px; }
  .title-the {
    position: absolute; right: 8px; top: 76px;
    color: var(--honey); font-weight: 300; font-size: 64px; letter-spacing: -4px; line-height: 1;
  }
  .title-word {
    position: absolute; right: -6px; writing-mode: vertical-rl;
    font-weight: 800; line-height: 0.86; white-space: nowrap;
  }
  .title-quiet { top: 142px; font-size: 128px; letter-spacing: -4px; color: var(--ink); }
  .title-fox { top: 552px; font-size: 138px; letter-spacing: -6px; color: var(--honey); }
  .opening-hours {
    position: absolute; left: 22px; top: 550px;
    font-weight: 800; font-size: 32px; line-height: 38px; letter-spacing: -1px; color: var(--ink);
  }

  /* Poster cards */
  .poster-card {
    position: absolute; border: 2px solid var(--rule); overflow: hidden; background: var(--paper);
  }
  .poster-card .brand-mark { position: absolute; right: 10px; top: 12px; font-size: 9px; gap: 4px; }
  .poster-card .brand-mark .dot { width: 14px; height: 14px; background: var(--honey); border: 3px solid var(--ink); }
  .poster-plain { left: 542px; top: 75px; width: 388px; height: 237px; }
  .poster-specials { left: 774px; top: 350px; width: 388px; height: 237px; }
  .poster-card .watermark-disc { width: 300px; height: 300px; }
  .poster-plain .watermark-disc { left: 40px; top: 80px; }
  .poster-specials .watermark-disc { left: 70px; top: 75px; }
  .poster-card .watermark { font-size: 30px; color: #e1e3e2; }
  .poster-plain .watermark { left: 110px; top: 170px; }
  .poster-specials .watermark { left: 140px; top: 165px; }
  .specials-band {
    position: absolute; left: 0; top: 0; bottom: 0; width: 40px; background: var(--ink);
    display: flex; align-items: flex-end; justify-content: center; padding-bottom: 6px;
  }
  .specials-band > .specials-label {
    writing-mode: vertical-rl; transform: rotate(180deg);
    color: var(--paper); font-weight: 800; font-size: 32px; letter-spacing: -0.5px; line-height: 1;
  }

  /* Shelf barkers */
  .shelf-barker {
    position: absolute; left: 443px; width: 719px; height: 107px;
    border: 2px solid var(--rule); overflow: hidden; background: var(--paper);
    display: flex; align-items: center; justify-content: flex-end; padding-right: 22px;
  }
  .shelf-barker .watermark-disc { left: 20px; top: 20px; width: 200px; height: 200px; }
  .barker-pay { top: 620px; }
  .barker-sandwiches { top: 763px; }
  .barker-label { position: relative; font-weight: 800; color: var(--ink); letter-spacing: -2px; }
  .barker-pay .barker-label { font-size: 54px; }
  .barker-sandwiches .barker-label { font-size: 66px; }
</style>
</head>
<body>
<main class="canvas">

  <section class="exterior-sign" aria-label="Exterior shop sign">
    <div class="site-band">HOSPITAL SHOP</div>
    <div class="watermark-disc"></div>
    <div class="watermark-disc watermark-soft"></div>
    <div class="brand-mark"><span class="dot"></span><span>The Quiet Fox</span></div>
    <div class="title-the">THE</div>
    <div class="title-word title-quiet">QUIET</div>
    <div class="title-word title-fox">FOX</div>
    <p class="opening-hours">OPENING<br>HOURS<br>8 AM<br>TO<br>9 PM<br>7 DAYS<br>A WEEK</p>
  </section>

  <section class="poster-card poster-plain" aria-label="Blank offer poster">
    <div class="watermark-disc"></div>
    <div class="watermark">The Quiet Fox</div>
    <div class="brand-mark"><span class="dot"></span><span>The Quiet Fox</span></div>
  </section>

  <section class="poster-card poster-specials" aria-label="Specials poster">
    <div class="specials-band"><span class="specials-label">SP<span class="accent">E</span>CIALS</span></div>
    <div class="watermark-disc"></div>
    <div class="watermark">The Quiet Fox</div>
    <div class="brand-mark"><span class="dot"></span><span>The Quiet Fox</span></div>
  </section>

  <section class="shelf-barker barker-pay" aria-label="Till sign">
    <div class="watermark-disc"></div>
    <span class="barker-label">PLEAS<span class="accent">E</span> PAY HER<span class="accent">E</span></span>
  </section>

  <section class="shelf-barker barker-sandwiches" aria-label="Sandwiches sign">
    <div class="watermark-disc"></div>
    <span class="barker-label">SANDWICH<span class="accent">E</span>S</span>
  </section>

</main>
</body>
</html>
```